LuMen Assembly. "Powering Enterprise Renewal" Website

I have established a new company based in Sydney Australia that exists to support large service companies to transform their businesses. I offer a bespoke alternative to the large consulting firms like QR, Ferrander, WHTC and Bramwell. My intention over time is to grow this business with more consulting partners and practitioners and expand into ASIA PAC, Europe and the US.

I would like to create a mobile responsive website that has a similar look and feel to QR, see URL below plus URLs for Bramwell, Ferrander and WHTC.

http://www.qr-example.com/
https://home.whtc-example.com/au/en/home.html
http://www.bramwell-example.com/

I am on a limited budget however so do not require a whole lot of fancy features. Key priorities;

- Responsive to all device types. PC, Tablet, Mobile
- A horizontal scrolling set of hero images that link to particular story or subject like QR-example.com. 3 only required
- Only limited content is required and most would be static apart from hero scrolling images/topics at top of page
- I would need the ability to be able to remove, replace, update the hero slides every 3-4 months
- Key priority is to present a level of professionalism and look and feel on par with QR, Ferrander, Bramwell and Co, for people to know what I do and how to contact me.
- Link site to my linked in Profile
- My logo is attached and contact details
- I have purchased the domain name www.lumenassembly-example.com.au through true registries
Updates

Industry/Entity Type

Management Consulting

Coding

Coded - Design and coding required

Number of Pages Required

1 page

Requirements
Must have
• Mobile responsive to be viewed on any device, simple clean design, easy to find contact details, 3 scrolling articles like QR-example.com that link to a PDF article. Align colours and theming to Logo on white background attached. Align fonts, look and feel etc to Log design attached

```html
<!DOCTYPE html>
<html lang="en">
<head>
<meta charset="utf-8">
<title>LuMen Assembly</title>
<link href="https://fonts.googleapis.com/css2?family=Montserrat:wght@400;500;600;700&display=swap" rel="stylesheet">
<style>
:root{
  --blue:#29a8e0;
  --ink:#1b1b1b;
  --muted:#8a8a8a;
  --rule:#dcdcdc;
  --panel:#f4f4f4;
  --white:#ffffff;
}
*{box-sizing:border-box;margin:0;padding:0}
html,body{width:1066px;height:1200px;overflow:hidden;background:var(--white)}
body{font-family:"Montserrat",sans-serif;color:var(--ink);position:relative}
a{color:inherit;text-decoration:none}
ul{list-style:none}

.site-header{position:absolute;left:0;top:0;width:1066px;height:67px;background:var(--panel);border-top:2px solid var(--blue)}
.brand{position:absolute;left:70px;top:20px;display:flex;align-items:center;gap:8px;font-size:19px;font-weight:500;color:#5a5a5a}
.brand-dot{width:12px;height:12px;border-radius:50%;background:var(--blue)}
.search{position:absolute;left:809px;top:10px;width:159px;height:22px;display:flex}
.search-field{flex:1;border:1px solid #d6d6d6;background:var(--white);font-size:10px;color:#aaa;padding:4px 5px}
.search-btn{width:23px;border:1px solid #d6d6d6;border-left:none;background:var(--white);display:flex;align-items:center;justify-content:center}
.menu-toggle{position:absolute;left:976px;top:15px}
.main-nav{position:absolute;right:70px;top:43px;display:flex;gap:16px;font-size:12px;font-weight:600;color:var(--blue)}

.frame{position:absolute;left:56px;top:67px;width:954px;height:1133px;border-left:1px solid var(--rule);border-right:1px solid var(--rule)}

.hero{position:absolute;left:70px;top:82px;width:926px;height:348px;background:radial-gradient(ellipse at 62% 45%,#8aa6b8 0%,#3f6a86 28%,#12263c 60%,#050d1a 100%)}
.hero-statement{position:absolute;left:68px;top:170px;width:275px;color:var(--white);font-size:17.5px;font-weight:700;line-height:22px}
.hero-arrow{position:absolute;top:157px;width:33px;height:33px;border-radius:50%;background:rgba(60,80,95,.75);display:flex;align-items:center;justify-content:center}
.hero-arrow.prev{left:8px}
.hero-arrow.next{right:8px}

.section-title{font-size:13px;font-weight:700;text-transform:uppercase;display:inline-block;padding-bottom:4px;border-bottom:2px solid var(--blue);min-width:107px}
.body-copy{font-size:10.4px;line-height:17.6px;color:var(--muted)}

.about{position:absolute;left:70px;top:450px;width:690px}
.about .body-copy{margin-top:4px}
.contact-card{position:absolute;left:776px;top:470px;width:220px;height:89px;background:var(--blue);color:var(--white);padding:6px 10px 6px 13px}
.contact-name{font-size:13.5px;font-weight:700;line-height:15px}
.contact-role{font-size:9.5px;font-weight:600}
.contact-line{display:flex;align-items:center;gap:7px;font-size:9.5px;font-weight:600;margin-top:8px;white-space:nowrap}
.contact-line.email{font-size:8.6px;gap:6px}
.contact-line+.contact-line{margin-top:7px}

.blog{position:absolute;left:70px;top:570px;width:926px}
.blog-grid{display:flex;gap:16px;margin-top:15px}
.post{width:220px}
.post:nth-child(2){margin-left:-1px}
.post-image{height:125px}
.post-image.city{background:linear-gradient(160deg,#d8e8f6,#6c9fd2 55%,#1f4f9a)}
.post-image.bulbs{background:radial-gradient(circle at 55% 30%,#f3e9c2,#9c8a5a 40%,#2a2418 80%)}
.post-image.desk{background:linear-gradient(160deg,#eef3f8,#bfcedc 60%,#8ea3b7)}
.post-image.laptop{background:linear-gradient(150deg,#e6e2de,#b5aaa0 55%,#7a6b60)}
.post-title{font-size:10.5px;font-weight:700;line-height:15px;margin-top:12px}
.post .body-copy{margin-top:6px;font-size:10.4px;line-height:14.5px}

.lower{position:absolute;left:70px;top:868px;width:926px;height:170px}
.locations{position:absolute;left:0;top:0;width:220px}
.location-list{margin-top:14px;border-top:1px solid var(--rule)}
.location-list li{height:22.3px;border-bottom:1px solid var(--rule);font-size:10.4px;font-weight:500;color:var(--blue);display:flex;align-items:center;gap:6px}
.location-list li::before,.footer-links li::before{content:"»";font-size:9px}
.news{position:absolute;left:235px;top:0;width:456px}
.news-item{margin-top:12px}
.news-item+.news-item{margin-top:15px}
.news-title{font-size:10.4px;font-weight:700;margin-bottom:2px}
.news .body-copy{line-height:13.5px}
.careers{position:absolute;left:706px;top:0;width:220px}
.careers .body-copy{margin-top:12px;line-height:14.8px}
.careers-email{margin-top:23px;height:25px;background:var(--blue);color:var(--white);font-size:9.4px;font-weight:600;display:flex;align-items:center;justify-content:center;gap:8px;white-space:nowrap}

.site-footer{position:absolute;left:57px;top:1058px;width:952px;height:142px;background:var(--panel);border-top:1px solid var(--rule)}
.footer-cols{position:absolute;left:13px;top:14px;display:flex}
.footer-col{width:235px}
.footer-col:nth-child(2){width:237px}
.footer-col h3{font-size:11.5px;font-weight:700;margin-bottom:4px}
.footer-links li{font-size:10.4px;color:var(--muted);line-height:19.2px;display:flex;gap:6px}
.footer-legal{position:absolute;left:0;top:111px;width:952px;border-top:1px solid var(--rule);text-align:center;font-size:8px;font-weight:600;color:#999;padding-top:9px}
</style>
</head>
<body>
<header class="site-header">
  <a class="brand" href="#"><span class="brand-dot"></span>LuMen Assembly</a>
  <form class="search">
    <span class="search-field">Search</span>
    <span class="search-btn"><svg width="13" height="13" viewBox="0 0 13 13"><circle cx="5.5" cy="5.5" r="4.3" fill="none" stroke="#aaa" stroke-width="1.4"/><line x1="8.6" y1="8.6" x2="12" y2="12" stroke="#aaa" stroke-width="1.6"/></svg></span>
  </form>
  <svg class="menu-toggle" width="20" height="15" viewBox="0 0 20 15"><rect y="0" width="20" height="3" fill="#666"/><rect y="6" width="20" height="3" fill="#666"/><rect y="12" width="20" height="3" fill="#666"/></svg>
  <nav class="main-nav"><a href="#">HOME</a><a href="#">INSIGHTS</a><a href="#">INDUSTRIES</a><a href="#">SERVICES</a><a href="#">CAREERS</a></nav>
</header>

<div class="frame"></div>

<section class="hero" role="img" aria-label="Hand holding a compass against a deep blue background">
  <p class="hero-statement">LuMen Assembly we believe in Finding the why. Finding a way, Deliver + 1, Giving back to people and teams, Leaving organisations in a better place.</p>
  <a class="hero-arrow prev" href="#" aria-label="Previous slide"><svg width="12" height="16" viewBox="0 0 12 16"><polyline points="9,1 2,8 9,15" fill="none" stroke="#fff" stroke-width="1.6"/></svg></a>
  <a class="hero-arrow next" href="#" aria-label="Next slide"><svg width="12" height="16" viewBox="0 0 12 16"><polyline points="3,1 10,8 3,15" fill="none" stroke="#fff" stroke-width="1.6"/></svg></a>
</section>

<section class="about">
  <h2 class="section-title">What we do</h2>
  <p class="body-copy">Lorem ipsum dolor sit amet, consectetur adipiscing elit, sed do eiusmod tempor incididunt ut labore at dolore magna aliqua. Ut enim ad minim veniam, quis nostrud exercitation ullamco laboris nisi ut aliquipex ea commodo consequat. Duis aute irure dolor in reprehen-derit in voluptate velit esse cillum dolore eu fugiat nulla pariatur. Excepteur sint occaecat cupidatat non proident, sunt in culpa qui offi-cia deserunt mollie anim id est laborum. Ut enim ad minim veniam, quis nostrud exercitation .</p>
</section>

<aside class="contact-card">
  <div class="contact-name">Rowan Pell</div>
  <div class="contact-role">Director</div>
  <div class="contact-line"><svg width="10" height="15" viewBox="0 0 10 15"><rect x="1" y="1" width="8" height="13" rx="1.5" fill="none" stroke="#fff" stroke-width="1.2"/><line x1="4" y1="12" x2="6" y2="12" stroke="#fff"/></svg>+61400000123</div>
  <div class="contact-line email"><svg width="14" height="10" viewBox="0 0 14 10"><rect x=".6" y=".6" width="12.8" height="8.8" fill="none" stroke="#fff" stroke-width="1.1"/><polyline points=".6,.6 7,6 13.4,.6" fill="none" stroke="#fff" stroke-width="1.1"/></svg>rowan@lumenassembly-example.com.au</div>
</aside>

<section class="blog">
  <h2 class="section-title">Blog articles</h2>
  <div class="blog-grid">
    <article class="post">
      <div class="post-image city" role="img" aria-label="Business figure among blue glass towers"></div>
      <h3 class="post-title">Sed volutpat ipsum in elit dignissim, eu pellentesque dolor rhoncus.</h3>
      <p class="body-copy">Eiusmod tempor incididunt ut labore at dolore magna aliqua. Ut enim ad minim veniam, quis nostrud exercitation</p>
    </article>
    <article class="post">
      <div class="post-image bulbs" role="img" aria-label="Row of light bulbs with one glowing"></div>
      <h3 class="post-title">Maecenas porta risus at ipsum vestibulum, eu lacinia ipsum tempor.</h3>
      <p class="body-copy">Eiusmod tempor incididunt ut labore at dolore magna aliqua. Ut enim ad minim veniam, quis nostrud exercitation</p>
    </article>
    <article class="post">
      <div class="post-image desk" role="img" aria-label="Glasses resting on a contract document"></div>
      <h3 class="post-title">Vivamus faucibus ex vel lorem rutrum, vitae scelerisque quam rhoncus.</h3>
      <p class="body-copy">Eiusmod tempor incididunt ut labore at dolore magna aliqua. Ut enim ad minim veniam, quis nostrud exercitation</p>
    </article>
    <article class="post">
      <div class="post-image laptop" role="img" aria-label="Hands typing on a laptop at a desk"></div>
      <h3 class="post-title">Ut et sapien sed augue fermentum consectetur sit amet vel turpis.</h3>
      <p class="body-copy">Eiusmod tempor incididunt ut labore at dolore magna aliqua. Ut enim ad minim veniam, quis nostrud exercitation</p>
    </article>
  </div>
</section>

<section class="lower">
  <div class="locations">
    <h2 class="section-title">Our locations</h2>
    <ul class="location-list">
      <li>Sydney, Australia</li><li>Asia</li><li>Pacific</li><li>Europe</li><li>United States of America</li>
    </ul>
  </div>
  <div class="news">
    <h2 class="section-title">News and events</h2>
    <div class="news-item">
      <h3 class="news-title">Lorem ipsum dolor sit amet, consectetur adipiscing elit</h3>
      <p class="body-copy">Sed do eiusmod tempor incididunt ut labore at dolore magna aliqua. Ut enim ad minim veniam, Lorem ipsum dolor sit amet, consectetur adipiscing elit, sed do.</p>
    </div>
    <div class="news-item">
      <h3 class="news-title">Vivamus faucibus ex vel lorem rutrum, vitae scelerisque quam rhoncus.</h3>
      <p class="body-copy">Sed do eiusmod tempor incididunt ut labore at dolore magna aliqua. Ut enim ad minim veniam, Lorem ipsum dolor sit amet, consectetur adipiscing elit. Vivamus fauci-bus ex vel lorem rutrum, vitae scelerisque quam rhoncus.</p>
    </div>
  </div>
  <div class="careers">
    <h2 class="section-title">Careers</h2>
    <p class="body-copy">Lorem ipsum dolor sit amet, consectetur adipiscing elit, sed do eiusmod tempor incididunt ut labore et dolore magna aliqua.</p>
    <a class="careers-email" href="#"><svg width="14" height="10" viewBox="0 0 14 10"><rect x=".6" y=".6" width="12.8" height="8.8" fill="none" stroke="#fff" stroke-width="1.1"/><polyline points=".6,.6 7,6 13.4,.6" fill="none" stroke="#fff" stroke-width="1.1"/></svg>info@lumenassembly-example.com.au</a>
  </div>
</section>

<footer class="site-footer">
  <div class="footer-cols">
    <div class="footer-col"><h3>ABOUT US</h3><ul class="footer-links"><li>Lorem ipsum dolor sit amet,</li><li>Sed volutpat ipsum in elit dignissim</li><li>Fusce ut libero eu nulla tincidunt</li></ul></div>
    <div class="footer-col"><h3>INSIGHTS</h3><ul class="footer-links"><li>Lorem ipsum dolor sit amet,</li><li>Sed volutpat ipsum in elit dignissim</li><li>Fusce ut libero eu nulla tincidunt</li></ul></div>
    <div class="footer-col"><h3>SERVICES</h3><ul class="footer-links"><li>Lorem ipsum dolor sit amet,</li><li>Sed volutpat ipsum in elit dignissim</li><li>Fusce ut libero eu nulla tincidun</li></ul></div>
    <div class="footer-col"><h3>INDUSTRIES</h3><ul class="footer-links"><li>Lorem ipsum dolor sit amet,</li><li>Sed volutpat ipsum in elit dignissim</li><li>Fusce ut libero eu nulla tincidunt</li></ul></div>
  </div>
  <p class="footer-legal">© 2016. ALL RIGHTS RESERVED</p>
</footer>
</body>
</html>
```